marlow pennant website Redesign

Read the Company mission statement and then help us redesign the website along the guidelines in the design brief and using the logo and fonts supplied.

The current marlow pennant website is very dated but has been very sucessful, we would like to invest in a brand refresh and site rebuild to bring the website up to 2018 standard.

We have using cut and paste from other travel websites made a pdf mock up of what sort of content we need on the pages and the lay out we like.

Target Market(s)

+45 Plus experienced Marlow Pennant, established, educated

Number of Pages Required

4 page

Font styles to use
Sans Serif

Requirements
Must have
• There is a full brief document and mock up, it must follow the brand guidelines
Nice to have
• There is a full brief document and mock up
Should not have
• Looks of a cheap cruise deal travel site

```html
<!DOCTYPE html>
<html lang="en">
<head>
<meta charset="utf-8">
<title>Marlow Pennant – Home</title>
<link href="https://fonts.googleapis.com/css2?family=Montserrat:wght@500;600;700;800&family=Poppins:wght@400;500;600&display=swap" rel="stylesheet">
<style>
:root{
  --green:#8cc63f;
  --brand-blue:#3b82c4;
  --navy:#1d4e8f;
  --ink:#222;
  --muted:#666;
  --band:#f2f2f2;
  --line:#e3e3e3;
  --field:#d9ecf8;
  --star:#f5c518;
}
*{box-sizing:border-box;margin:0;padding:0}
html,body{width:1200px;height:3199px;overflow:hidden;background:#fff}
body{position:relative;font-family:'Poppins',sans-serif;color:var(--ink);font-size:11px}
.abs{position:absolute}
.heading{font-family:'Montserrat',sans-serif;font-weight:700;font-size:17px;letter-spacing:.5px;text-transform:uppercase;text-align:center;color:#222}

/* header */
.logo{left:183px;top:16px;font-family:'Montserrat',sans-serif;font-weight:600;color:var(--brand-blue);line-height:1}
.logo .main{font-size:30px;letter-spacing:1px;text-transform:uppercase}
.logo .sub{font-size:14px;color:var(--green);font-weight:500;margin-top:2px;border-top:1px solid var(--brand-blue);display:inline-block;padding-top:2px}
.newsletter-btn{left:911px;top:21px;width:122px;height:24px;background:var(--green);color:#fff;font-size:10px;font-weight:600;display:flex;align-items:center;justify-content:center}
.contact-phone{left:811px;top:55px;font-size:13px;font-weight:600;display:flex;align-items:center;gap:6px}
.social{display:flex;gap:6px}
.social span{width:14px;height:14px;border-radius:50%;background:var(--navy)}
.social span.outline{background:none;border:1.5px solid #333}
.header-social{left:940px;top:58px}
.nav-rule{left:83px;top:88px;width:1051px;height:1px;background:var(--green)}
.nav{left:183px;top:98px;width:850px;display:flex;font-family:'Montserrat',sans-serif;font-weight:700;font-size:11px;text-transform:uppercase;color:#222}
.nav a{color:inherit;text-decoration:none;margin-right:31px}
.nav a.active{color:var(--green)}
.nav .right{margin-left:auto;display:flex;gap:20px}
.nav .right a{margin:0;color:var(--navy)}

/* hero */
.hero{left:83px;top:128px;width:1051px;height:282px;background:linear-gradient(180deg,#cfe9ea 0%,#b9dbd8 45%,#8aa5a0 70%,#58705f 100%)}
.hero-search{left:399px;top:194px;width:413px;height:88px;background:rgba(80,95,95,.55);padding:12px 22px}
.hero-search h2{font-family:'Montserrat',sans-serif;font-weight:700;font-size:13px;color:#fff;text-align:center;letter-spacing:.5px;margin-bottom:8px}
.hero-input{display:flex;height:28px;border-radius:14px;overflow:hidden;background:#fff}
.hero-input .go{width:48px;background:var(--green);display:flex;align-items:center;justify-content:center}
.hero-input .text{flex:1;display:flex;align-items:center;padding-left:10px;font-size:10px;color:#555}
.hero-toggle{left:580px;top:394px;width:36px;height:20px;border-radius:18px 18px 0 0;background:#fff;display:flex;justify-content:center;padding-top:5px}
.filter-band{left:83px;top:410px;width:1051px;height:112px;background:linear-gradient(180deg,#3f8fcd,#2c75b4)}
.filters{left:183px;top:443px;width:850px;display:grid;grid-template-columns:repeat(4,1fr);gap:10px 12px}
.select{height:28px;background:var(--field);border-radius:3px;font-size:10px;font-weight:600;padding:0 9px;display:flex;align-items:center;justify-content:space-between;color:#1e2b3a}
.select.search{background:var(--navy);color:#fff}

/* welcome */
.welcome-title{left:0;top:570px;width:1200px}
.welcome-text{left:330px;top:612px;width:540px;text-align:center;font-size:10.5px;line-height:1.6;color:#444}
.review{left:183px;top:718px;width:850px;display:flex;align-items:center}
.stars{display:flex;gap:10px;margin-right:22px}
.review q{font-style:italic;font-weight:600;font-size:11px;quotes:"\201C" "\201D"}
.review .by{font-size:9px;color:var(--muted);margin-left:8px}
.review .all{margin-left:auto;color:var(--navy);font-weight:600;font-size:10px;text-decoration:underline}

/* features box */
.feature-box{left:183px;top:778px;width:850px;height:342px;background:var(--band)}
.feature{position:absolute;left:183px;display:flex;gap:20px}
.feature .photo{width:216px;height:84px}
.feature h3{font-family:'Montserrat',sans-serif;font-weight:700;font-size:11px;text-transform:uppercase;margin-bottom:5px}
.feature h3::after{content:"";display:block;width:18px;height:2px;background:var(--green);margin-top:4px}
.feature p{width:240px;font-size:10px;line-height:1.6;color:#444}
.feature .more{display:block;margin-top:12px;font-family:'Montserrat',sans-serif;font-weight:700;font-size:9.5px;text-transform:uppercase}

/* carousels */
.arrow{position:absolute;width:36px;height:36px;border-radius:50%;border:1.5px solid #555;background:#fff;display:flex;align-items:center;justify-content:center}
.journey-title{left:0;top:1200px;width:1200px}
.card-row{left:183px;width:850px;display:flex;gap:18px}
.journey{width:199px;height:197px;background:#fff;box-shadow:0 3px 10px rgba(0,0,0,.12)}
.journey .photo{height:126px}
.journey .info{padding:8px 10px;display:grid;grid-template-columns:1fr auto;row-gap:4px;font-size:10px}
.journey .name{font-family:'Montserrat',sans-serif;font-weight:700;font-size:11px}
.journey .from{font-size:8px;color:var(--muted);text-align:right;align-self:end}
.journey .days{color:var(--muted);display:flex;align-items:center;gap:4px}
.journey .price{color:#333}

.exp-band{left:75px;top:1487px;width:1059px;height:296px;background:var(--band)}
.exp-title{left:0;top:1533px;width:1200px}
.exp{width:198px;text-align:center}
.exp .photo{height:145px}
.exp .label{margin-top:12px;font-family:'Montserrat',sans-serif;font-weight:700;font-size:11px}

/* marketing */
.mkt-title{left:0;top:1827px;width:1200px}
.magazines{left:183px;top:1873px;width:850px;display:flex;gap:10px}
.magazine{flex:1;height:356px;box-shadow:0 8px 16px rgba(0,0,0,.3)}

/* regions */
.region-band{left:75px;top:2274px;width:1059px;height:405px;background:var(--band)}
.region-title{left:0;top:2318px;width:1200px}
.region{width:199px;height:269px;background:#fff}
.region .photo{height:143px}
.region .body{padding:12px 12px}
.region h4{font-family:'Montserrat',sans-serif;font-weight:700;font-size:11px;margin-bottom:6px}
.region p{font-size:10px;line-height:1.55;color:#444}

/* partners */
.partners{left:183px;top:2728px;width:850px;display:flex;justify-content:space-between;align-items:center;padding:0 20px;height:32px}
.partner{font-family:'Montserrat',sans-serif;font-weight:700;font-size:14px;color:var(--navy);display:flex;align-items:center;gap:6px}
.partner i{width:12px;height:12px;background:var(--navy);display:inline-block}
.partners-rule{left:83px;top:2800px;width:1051px;height:1px;background:var(--line)}

/* footer */
.footer-col{position:absolute;top:2841px;font-size:10px;color:#333}
.footer-col h5{font-family:'Montserrat',sans-serif;font-weight:700;font-size:13px;margin-bottom:12px;color:#222}
.footer-col h5::after{content:"";display:block;width:18px;height:2px;background:var(--green);margin-top:4px}
.link-cols{display:flex;gap:42px}
.link-cols ul{list-style:none;line-height:2.15;font-size:9.5px}
.link-cols li::before{content:"› "}
.footer-col p{line-height:1.55}
.illustration{margin-top:10px;width:205px;height:112px;background:linear-gradient(135deg,#5cc8d0,#3bb4c0)}
.field-label{font-size:9px;font-weight:600;margin:8px 0 3px;text-transform:uppercase}
.field{width:195px;height:20px;border-radius:10px;background:#eee;font-size:8.5px;color:#888;display:flex;align-items:center;padding-left:10px}
.subscribe{margin-top:12px;width:104px;height:22px;background:var(--green);color:#fff;font-size:9.5px;font-weight:600;display:flex;align-items:center;justify-content:center}
.contact-list{list-style:none;line-height:1.55}
.contact-list li{display:flex;gap:10px;align-items:flex-start;margin-bottom:8px}
.contact-list .big{font-family:'Montserrat',sans-serif;font-weight:700;font-size:14px}
.bottom-bar{left:75px;top:3120px;width:1059px;height:42px;background:var(--band)}
.bottom-logo{left:183px;top:3124px;font-family:'Montserrat',sans-serif;font-weight:600;color:var(--brand-blue);line-height:1}
.bottom-logo .main{font-size:20px;text-transform:uppercase;letter-spacing:1px}
.bottom-logo .sub{font-size:9px;color:var(--green)}
.copyright{left:913px;top:3135px;font-size:10px;color:#333}
</style>
</head>
<body>

<header>
  <div class="abs logo"><div class="main">Marlow</div><div class="sub">Pennant</div></div>
  <div class="abs newsletter-btn">Newsletter Subscribe</div>
  <div class="abs contact-phone">
    <svg width="16" height="16" viewBox="0 0 16 16"><circle cx="8" cy="8" r="7" fill="none" stroke="#333" stroke-width="1.2"/><path d="M5.5 4.5l1.5 0 .7 1.8-.9.7a5 5 0 0 0 2.2 2.2l.7-.9 1.8.7v1.5c-3.5.3-6.3-2.5-6-6z" fill="#333"/></svg>
    0800 40 62 19
  </div>
  <div class="abs social header-social"><span></span><span></span><span></span><span class="outline"></span></div>
  <div class="abs nav-rule"></div>
  <nav class="abs nav">
    <a class="active">Home</a><a>About Us</a><a>Our Cruises</a><a>Destinations</a><a>Exclusive</a><a>Offers</a><a>Brochures</a>
    <div class="right"><a>Our Team</a><a>Contact</a></div>
  </nav>
</header>

<section class="hero-section">
  <div class="abs hero" role="img" aria-label="Photo of a mountain rising above a calm bay under a pale sky"></div>
  <div class="abs hero-search">
    <h2>TRAVEL WITH PERSONALITY</h2>
    <div class="hero-input">
      <div class="go"><svg width="14" height="14" viewBox="0 0 14 14"><circle cx="6" cy="6" r="4" fill="none" stroke="#fff" stroke-width="1.8"/><path d="M9 9l3.5 3.5" stroke="#fff" stroke-width="1.8"/></svg></div>
      <div class="text">Where do you feel like going?</div>
    </div>
  </div>
  <div class="abs filter-band"></div>
  <div class="abs hero-toggle"><svg width="12" height="8" viewBox="0 0 12 8"><path d="M1 1l5 5 5-5" fill="none" stroke="#333" stroke-width="2"/></svg></div>
  <div class="abs filters">
    <div class="select">Any Destination<span>▾</span></div>
    <div class="select">Any Sailing Date<span>▾</span></div>
    <div class="select">Any Length<span>▾</span></div>
    <div class="select">Any Cruise Line<span>▾</span></div>
    <div class="select">Any Cruise Ship<span>▾</span></div>
    <div class="select">Any Departure Port<span>▾</span></div>
    <div class="select">Any Price Range<span>▾</span></div>
    <div class="select search">Search Cruises<span>▾</span></div>
  </div>
</section>

<section class="welcome">
  <h1 class="abs heading welcome-title">Welcome to Marlow Pennant</h1>
  <p class="abs welcome-text">Nunc id nulla elit. Fusce sit amet convallis leo, sed sollicitudin mauris. Vestibulum ornare odio vitae tincidunt tempor. Praesent a ligula ex. Aenean eleifend neque turpis. Ut mattis egestas urna sed finibus Aenean eleifend nequ.</p>
  <div class="abs review">
    <div class="stars">
      <svg width="14" height="14" viewBox="0 0 24 24"><path d="M12 2l3 7 7 .6-5.4 4.7 1.7 7.2L12 17.8 5.7 21.5l1.7-7.2L2 9.6 9 9z" fill="var(--star)"/></svg>
      <svg width="14" height="14" viewBox="0 0 24 24"><path d="M12 2l3 7 7 .6-5.4 4.7 1.7 7.2L12 17.8 5.7 21.5l1.7-7.2L2 9.6 9 9z" fill="var(--star)"/></svg>
      <svg width="14" height="14" viewBox="0 0 24 24"><path d="M12 2l3 7 7 .6-5.4 4.7 1.7 7.2L12 17.8 5.7 21.5l1.7-7.2L2 9.6 9 9z" fill="var(--star)"/></svg>
      <svg width="14" height="14" viewBox="0 0 24 24"><path d="M12 2l3 7 7 .6-5.4 4.7 1.7 7.2L12 17.8 5.7 21.5l1.7-7.2L2 9.6 9 9z" fill="var(--star)"/></svg>
      <svg width="14" height="14" viewBox="0 0 24 24"><path d="M12 2l3 7 7 .6-5.4 4.7 1.7 7.2L12 17.8 5.7 21.5l1.7-7.2L2 9.6 9 9z" fill="var(--star)"/></svg>
    </div>
    <q>Friendly reliable trust great to deal with,</q><span class="by">R.Hale, Leeds</span>
    <span class="all">See all review →</span>
  </div>
</section>

<section class="features">
  <div class="abs feature-box"></div>
  <div class="feature" style="left:366px;top:804px">
    <div class="photo" role="img" aria-label="Photo of a riverside old town at dusk" style="background:linear-gradient(180deg,#4f7fc0,#2d4f86 60%,#a07a45)"></div>
    <div>
      <h3>Small ships are best</h3>
      <p>Nunc id nulla elit. Fusce sit amet convallis leo, sed sollicitudin mauris. Vestibulum ornare odio vitae tincidunt tempor. Praesent a ligula ex. Aenean eleifend.</p>
      <span class="more">Discover our range →</span>
    </div>
  </div>
  <div class="feature" style="left:366px;top:960px">
    <div class="photo" role="img" aria-label="Photo of a warm hotel lounge with a fireplace" style="background:linear-gradient(135deg,#d9b58a,#8a5a36 60%,#c89a6a)"></div>
    <div>
      <h3>You won't find it elsewhere</h3>
      <p>Nunc id nulla elit. Fusce sit amet convallis leo, sed sollicitudin mauris. Vestibulum ornare odio vitae tincidunt tempor. Praesent a ligula ex. Aenean eleifend.</p>
      <span class="more">Discover our range →</span>
    </div>
  </div>
</section>

<section class="journeys">
  <h2 class="abs heading journey-title">Featured Journeys</h2>
  <div class="arrow" style="left:117px;top:1315px"><svg width="10" height="12" viewBox="0 0 10 12"><path d="M7 1L2 6l5 5" fill="none" stroke="#333" stroke-width="1.6"/></svg></div>
  <div class="arrow" style="left:1058px;top:1315px"><svg width="10" height="12" viewBox="0 0 10 12"><path d="M3 1l5 5-5 5" fill="none" stroke="#333" stroke-width="1.6"/></svg></div>
  <div class="abs card-row" style="top:1245px">
    <div class="journey"><div class="photo" role="img" aria-label="Photo of carved temple statues among trees" style="background:linear-gradient(160deg,#7e8a5a,#4e4a34)"></div>
      <div class="info"><span class="name">Amazon Cruise</span><span class="from">FROM</span><span class="days">◷ 4 Day / 3 Nights</span><span class="price">$2,470</span></div></div>
    <div class="journey"><div class="photo" role="img" aria-label="Photo of a bright hotel bedroom" style="background:linear-gradient(160deg,#e6d3b6,#a98458)"></div>
      <div class="info"><span class="name">Amazon Cruise</span><span class="from">FROM</span><span class="days">◷ 4 Day / 3 Nights</span><span class="price">$2,470</span></div></div>
    <div class="journey"><div class="photo" role="img" aria-label="Photo of a white villa with a pool" style="background:linear-gradient(180deg,#6aa4d8,#e8e2d4 55%,#39b7d6)"></div>
      <div class="info"><span class="name">Amazon Cruise</span><span class="from">FROM</span><span class="days">◷ 4 Day / 3 Nights</span><span class="price">$2,470</span></div></div>
    <div class="journey"><div class="photo" role="img" aria-label="Photo of a busy beach by a coastal town" style="background:linear-gradient(180deg,#9cc6e6,#d9c7a8 55%,#4a9cc8)"></div>
      <div class="info"><span class="name">Amazon Cruise</span><span class="from">FROM</span><span class="days">◷ 4 Day / 3 Nights</span><span class="price">$2,470</span></div></div>
  </div>
</section>

<section class="experiences">
  <div class="abs exp-band"></div>
  <h2 class="abs heading exp-title">Amazing Range of Experiences</h2>
  <div class="arrow" style="left:117px;top:1638px"><svg width="10" height="12" viewBox="0 0 10 12"><path d="M7 1L2 6l5 5" fill="none" stroke="#333" stroke-width="1.6"/></svg></div>
  <div class="arrow" style="left:1058px;top:1638px"><svg width="10" height="12" viewBox="0 0 10 12"><path d="M3 1l5 5-5 5" fill="none" stroke="#333" stroke-width="1.6"/></svg></div>
  <div class="abs card-row" style="top:1578px">
    <div class="exp"><div class="photo" role="img" aria-label="Photo of half-timbered houses along a canal" style="background:linear-gradient(180deg,#a9c8e4,#8b6a4a 55%,#5c6a55)"></div><div class="label">River Cruises</div></div>
    <div class="exp"><div class="photo" role="img" aria-label="Photo of a bathtub by a window over the sea" style="background:linear-gradient(180deg,#5f4a3a,#7fc4d8 40%,#d8d2c8)"></div><div class="label">Expedition Cruises</div></div>
    <div class="exp"><div class="photo" role="img" aria-label="Photo of a traveller reading a map" style="background:linear-gradient(160deg,#c9a27a,#6e5240)"></div><div class="label">Fly Free Cruises</div></div>
    <div class="exp"><div class="photo" role="img" aria-label="Photo of half-timbered houses along a canal" style="background:linear-gradient(180deg,#a9c8e4,#8b6a4a 55%,#5c6a55)"></div><div class="label">River Cruises</div></div>
  </div>
</section>

<section class="marketing">
  <h2 class="abs heading mkt-title">Recent Marketing</h2>
  <div class="abs magazines">
    <div class="magazine" role="img" aria-label="Travel magazine cover with a boat on a flower-lined river" style="background:linear-gradient(180deg,#3f9a8a,#2c6f7a 50%,#c9577a)"></div>
    <div class="magazine" role="img" aria-label="Travel magazine cover with overwater villas in a turquoise lagoon" style="background:linear-gradient(180deg,#cfe3ea,#3fbfc0 50%,#1e8f9a)"></div>
    <div class="magazine" role="img" aria-label="Travel magazine cover with a pagoda under a blue sky" style="background:linear-gradient(180deg,#f2c21a 0 14%,#2f6fc0 14%,#4a8fd0 60%,#b83a2a)"></div>
  </div>
</section>

<section class="regions">
  <div class="abs region-band"></div>
  <h2 class="abs heading region-title">Feature Regions</h2>
  <div class="abs card-row" style="top:2363px">
    <div class="region"><div class="photo" role="img" aria-label="Photo of pink roses against a white house" style="background:linear-gradient(160deg,#e9eef2,#c8a0a8 55%,#6f8a5a)"></div>
      <div class="body"><h4>River Cruises</h4><p>Nunc id nulla elit. Fusce sit amet convallis leo, sed sollicitudin mauris. Vestibulum ornare odio vitae</p></div></div>
    <div class="region"><div class="photo" role="img" aria-label="Photo of cyclists on a leafy country path" style="background:linear-gradient(180deg,#8fb25a,#4e7a32)"></div>
      <div class="body"><h4>River Cruises</h4><p>Nunc id nulla elit. Fusce sit amet convallis leo, sed sollicitudin mauris. Vestibulum ornare odio vitae</p></div></div>
    <div class="region"><div class="photo" role="img" aria-label="Photo of a temple interior in warm light" style="background:linear-gradient(160deg,#7a5a3a,#c48a4a 60%,#4a3526)"></div>
      <div class="body"><h4>River Cruises</h4><p>Nunc id nulla elit. Fusce sit amet convallis leo, sed sollicitudin mauris. Vestibulum ornare odio vitae</p></div></div>
    <div class="region"><div class="photo" role="img" aria-label="Photo of a pier over the sea at sunset" style="background:linear-gradient(180deg,#4a6fa8,#e8a86a 55%,#3a5a88)"></div>
      <div class="body"><h4>River Cruises</h4><p>Nunc id nulla elit. Fusce sit amet convallis leo, sed sollicitudin mauris. Vestibulum ornare odio vitae</p></div></div>
  </div>
</section>

<section class="partner-strip">
  <div class="arrow" style="left:117px;top:2726px"><svg width="10" height="12" viewBox="0 0 10 12"><path d="M7 1L2 6l5 5" fill="none" stroke="#333" stroke-width="1.6"/></svg></div>
  <div class="arrow" style="left:1058px;top:2726px"><svg width="10" height="12" viewBox="0 0 10 12"><path d="M3 1l5 5-5 5" fill="none" stroke="#333" stroke-width="1.6"/></svg></div>
  <div class="abs partners">
    <span class="partner"><i></i>Vantorly</span>
    <span class="partner">Brindlecap</span>
    <span class="partner"><i></i>Corvastack</span>
    <span class="partner">Tellumo</span>
    <span class="partner"><i></i>Pinaxa</span>
  </div>
  <div class="abs partners-rule"></div>
</section>

<footer>
  <div class="footer-col" style="left:183px">
    <h5>Discover World Journey</h5>
    <div class="link-cols">
      <ul><li>Home</li><li>Brochure</li><li>Home</li><li>Contact</li><li>Home</li><li>Term</li></ul>
      <ul><li>Cruise</li><li>Special offer</li><li>Home</li><li>Meet our team</li><li>Home</li><li>Privacy Policy</li></ul>
    </div>
  </div>
  <div class="footer-col" style="left:402px;width:200px">
    <h5>Welcome to our World</h5>
    <p>Nunc id nulla elit. Fusce sit amet convallis leo, sed sollicitudin mauris. Vestibulum ornare odio vitae tincidunt tempor. Praesent a ligula ex. Aenean eleifend.</p>
    <div class="illustration" role="img" aria-label="Illustration of an aeroplane surrounded by travel icons"></div>
  </div>
  <div class="footer-col" style="left:619px;width:200px">
    <h5>Mailing List</h5>
    <p>sed sollicitudin mauris sed sollicitudin mauris.sed s</p>
    <div class="field-label">Email</div><div class="field">Your email address</div>
    <div class="field-label">First Name</div><div class="field">Your first name</div>
    <div class="field-label">Last Name</div><div class="field">Your last name</div>
    <div class="subscribe">Subscribe</div>
  </div>
  <div class="footer-col" style="left:835px;width:200px">
    <ul class="contact-list">
      <li class="big"><svg width="14" height="14" viewBox="0 0 16 16"><path d="M3 1h3l1.5 4-2 1.5a9 9 0 0 0 4 4L11 8.5l4 1.5v3c-7 1-14-6-12-12z" fill="#333"/></svg>0800 40 62 19</li>
      <li><svg width="12" height="12" viewBox="0 0 16 16"><path d="M3 1h3l1.5 4-2 1.5a9 9 0 0 0 4 4L11 8.5l4 1.5v3c-7 1-14-6-12-12z" fill="#333"/></svg>09 360 4127</li>
      <li><svg width="12" height="12" viewBox="0 0 16 16"><rect x="1" y="3" width="14" height="10" fill="none" stroke="#333" stroke-width="1.4"/><path d="M3 6h10M3 9h6" stroke="#333"/></svg>09 360 4128</li>
      <li><svg width="12" height="12" viewBox="0 0 16 16"><rect x="1" y="3" width="14" height="10" fill="none" stroke="#333" stroke-width="1.4"/><path d="M1 3l7 6 7-6" fill="none" stroke="#333" stroke-width="1.4"/></svg>hello@marlowpennant.co</li>
      <li><svg width="12" height="14" viewBox="0 0 12 16"><path d="M6 1a5 5 0 0 0-5 5c0 4 5 9 5 9s5-5 5-9a5 5 0 0 0-5-5z" fill="none" stroke="#333" stroke-width="1.4"/><circle cx="6" cy="6" r="1.8" fill="#333"/></svg>sed sollicitudin mauris.sed sollicitudin mauris.sed s</li>
    </ul>
    <div class="social" style="margin-left:22px"><span></span><span></span><span></span><span class="outline"></span></div>
  </div>
  <div class="abs bottom-bar"></div>
  <div class="abs bottom-logo"><div class="main">Marlow</div><div class="sub">Pennant</div></div>
  <div class="abs copyright">© Marlow Pennant 2018</div>
</footer>

</body>
</html>
```